Zelmor Africa - Website Design Brief

Web Design Brief

ZELMOR AFRICA
WEBSITE DESIGN BRIEF

INTRODUCTION
ABOUT ZELMOR
• ZELMOR is a premier consulting firm that specialises in aiding global corporations and emerging businesses to enter and scale within Africa's dynamic markets. Through swift, actionable insights and innovative strategies, ZELMOR empowers clients to capitalise on Africa's untapped potential, thereby catering specifically to forward-thinking entities poised for exponential growth.

TASK DESCRIPTION
• Develop a 5-page website for ZELMOR.
• The primary goal is to present a clear and concise picture of our consulting firm, its Africa-centric experience, and its offerings to multinational clients looking for a professional partner to penetrate African markets or reclaim lost market share.

WEBSITE FRAMEWORK
Page Architecture:
• Home
o A powerful landing page that instantly communicates who ZELMOR is and what solutions it provides. Incorporate impactful visuals and calls-to-action.
• About
o A compelling narrative that illustrates ZELMOR's unique approach to consulting, dedication to Africa, and experience assisting multinational firms.
• Services
o A showcase of ZELMOR's successful projects and client testimonials. This page should build trust and credibility, demonstrating ZELMOR's ability to deliver exceptional results.
• Team
o Introduce up to 8 key team members, with each profile featuring a professional photo, name, title, and a brief bio showcasing the individual's skills, experiences, and contributions to ZELMOR's mission.
• Contact
o Clear and easy ways for visitors to contact ZELMOR for more information or to initiate a partnership.
• Footer
o Links to ZELMOR's social media profiles on Instagram and LinkedIn, along with a privacy policy.
o Social links
o Instagram: https://www.instagram.com/zelmorafrica/
o LinkedIn: https://www.linkedin.com/company/zelmorafrica/
o Privacy Policy
o Insert placeholder "lorem ipsum" text.
o Text will be provided with the revision round or ZELMOR will update text on site handover.

DESIGN INSPIRATION
• The website's design should evoke professionalism and elegance, with simple and clean lines inspired by site pages like:
o https://quendaro.example/
o https://quendaro.example/services/
o One aspect we particularly appreciate is how visitors can easily navigate by scrolling down to find what they're looking for and see everything they need to in an intuitive way on the home page
o What we don’t like about this site is how they navigate from the home page to other random pages – we like about to take you to the about page, and so on.

Branding Guidelines:
• See logo on Pixel Bazaar: Design #: 58170926
• We like the idea of the logo being black or white and have uploaded these options as well.
• Monochrome themes, with spots or splash of colour to highlight something is a style we appreciate.

Website Objectives and Goals:
• Our website's primary goal is to create a strong online presence, acting as a hub for potential clients to discover our credibility, reliability, and our ability to deliver exceptional results. It's essential that our website portrays professionalism, instils trustworthiness, and showcases our sincere dedication to Africa.

Target audience:
• ZELMOR's audience consists of businesses in mobile money, gaming, FMCG, beverage, and alcohol sectors, primarily Business Development Managers or Operations Managers who are seeking insight into their respective marketplaces.

Company Overview:
• ZELMOR stands out from the crowd as a consulting firm with a difference. Our dynamic team is fully dedicated to one mission: brand development within Africa.
• Unlike other companies that focus solely on online connectivity, we recognize the tremendous value in embracing the vibrant street culture that makes Africa so unique. Community engagement, empowerment, and expansion are at the forefront of everything we do.
• we recognize that unlocking business growth starts with a deep understanding of consumer behavior. It is this understanding that bridges the gap between companies and the communities that drive the cash economy. Our purpose is to reconnect businesses with the vibrant pulse of these essential local markets, injecting fresh vitality into their brands and propelling them towards resounding success in Africa.

Development to include:
• Basic SEO Setup:
o The website should be optimized for search engines, incorporating keywords, meta tags, and alt tags for images.
• Google Analytics Setup.
o To track website traffic and user behaviour for ongoing optimization.
• Google Crawling Setup
o The website needs to be easily indexed by Google, allowing it to appear in search results, and updated information effectively crawled by Google SEO and AHREFS scores.

PAGE CONTENT:
Home Page
• Background
o Option #1
o 4K video on home page, running on loop
o Bold Statement Text over Video
o Option #2
o Still Image
o Animated text making bold statement (e.g. our motto)

• Sections
o Contrast colour blocks or a way of making it clear that the next topic is a new topic.
o 5 sections
1. Home Main - Video + bold statement text
2. About - A paragraph and visual about us (lorem ipsum) that has a click through to our About Page (ignore how quendaro.example navigate, we think this is too complicated for our needs)
3. Services – communicated in some simple and powerful ways (we leave this open to you) – but keeping in mind it needs to be concise and professional.
4. Other - Something about our process that makes us unique (lorem ipsum text) and a placeholder image/animation.
5. Contact – a call-to-action button that takes you to our contact, but showcases a mobile number and email address.
6. Footer – as described in the previous section – placeholder for Instagram and LinkedIn only.

About Page
• Don’t reference quendaro.example for this page.
• Main Section
o Bold statements and images
• History Section
o A story about us and our past
• Final Section
o Some of our comments and final thoughts

Services Page
• How https://quendaro.example/services/ is laid out is great – we prefer a light theme.
• 6 - 8 x icons with headings and a brief description text box, and a read more drop down – all as placeholders to be edited later.
• For ease of direction for this page, look to the link shared above.

Team
• Add Placeholders for up to 8 team members (we only have 4 now):
o Image placeholder
o Name placeholder
o Title placeholder
o Short Bio (lorem ipsum)

Contact
• Clear and easy ways for visitors to contact ZELMOR for more information or to initiate a partnership.

• Insert placeholder "lorem ipsum" text, we will provide the text with our revision round.
o Ideally an easy form process that gives the user some options or dropdowns to complete before submission – up to 3 would be sufficient.
o Require their name and contact details.

NOTE: Images to follow:

Target Market(s)

ZELMOR's audience consists of businesses in mobile money, gaming, FMCG, beverage, and alcohol sectors, primarily Business Development Managers or Operations Managers who are seeking insight into their respective marketplaces.

Industry/Entity Type

ZELMOR is a premier consulting firm that specialises in aiding global corporations and emerging businesses to enter and scale within Africa's dynamic markets

Coding

Coded - Design and coding required

Number of Pages Required

5+ page

Font styles to use
Sans Serif
Other font styles liked:
• Poppins Font Family

Colors

Designer to choose colors to be used in the design.

Requirements
Must have
• The primary goal is to present a clear and concise picture of our consulting firm, and it's specialisation in Africa - smooth and crisp UI with animations or transitions that imply we know our way around tecchnology is always helpful - but a Clean and responsive UI is most important.
Nice to have
• Reactive and animated transitions through sections or pages - not overdone - adds a professional feel to the site
Should not have
• We don't want too many colours, and we don't want it too dark - we want a monochrome theme, with accents of colour when relevant

```html
<!DOCTYPE html>
<html lang="en">
<head>
<meta charset="utf-8">
<title>ZELMOR Consulting Firm</title>
<link rel="stylesheet" href="https://fonts.googleapis.com/css2?family=Roboto:wght@700;900&family=Raleway:wght@400;500;600;700;800&family=Lato:wght@400;700;900&display=swap">
<style>
:root{
  --navy:#020d1e;
  --deep:#0a1a48;
  --blue:#0a64c8;
  --blue-line:#1170d6;
  --ink:#0b1d6b;
  --white:#ffffff;
  --soft:#cfdcf0;
  --teal:#0fa99a;
  --muted:#5a6270;
}
*{margin:0;padding:0;box-sizing:border-box}
html,body{width:1200px;height:3757px;overflow:hidden}
body{position:relative;background:var(--white);font-family:"Raleway",sans-serif;color:var(--white)}
.abs{position:absolute}
.backdrop{position:absolute;left:0;top:0}
.hero-photo{left:0;top:0;width:1200px;height:745px;background:radial-gradient(ellipse at 50% 40%,#3d5066 0%,#253449 45%,#1a2433 100%)}
.logo{display:flex;align-items:center;gap:10px;font-family:"Raleway",sans-serif;font-weight:600;color:var(--white);letter-spacing:1px}
.logo-mark{border:4px solid var(--white);display:block}
.site-logo{left:108px;top:45px;font-size:42px}
.site-logo .logo-mark{width:46px;height:46px}
.nav{top:58px;font-family:"Lato",sans-serif;font-weight:700;font-size:15px;letter-spacing:.5px;color:var(--soft)}
.nav.active{color:var(--white)}
.nav.active::after{content:"";position:absolute;left:0;right:0;top:26px;height:2px;background:var(--white)}
.btn{display:flex;align-items:center;justify-content:center;border-radius:30px;font-family:"Lato",sans-serif;font-weight:700;letter-spacing:.5px;color:var(--white)}
.btn-contact{left:943px;top:44px;width:149px;height:48px;background:var(--blue);font-size:16px}
.play{left:563px;top:256px;width:72px;height:72px;border-radius:50%;background:var(--blue)}
.hero-kicker{left:0;width:1200px;top:348px;text-align:center;font-family:"Roboto",sans-serif;font-weight:700;font-size:30px}
.hero-title{left:0;width:1200px;top:388px;text-align:center;font-family:"Roboto",sans-serif;font-weight:700;font-size:50px}
.btn-hero{left:510px;top:475px;width:180px;height:48px;background:var(--blue);font-size:15px}
.section-title{font-family:"Roboto",sans-serif;font-weight:700;font-size:38px}
.about-title{left:162px;top:862px}
.body-text{font-size:15.5px;line-height:23px}
.about-text{left:162px;top:920px;width:392px}
.about-text p+p{margin-top:15px}
.btn-outline{left:162px;top:1112px;width:189px;height:50px;background:var(--white);border:3px solid var(--blue);color:var(--navy);font-weight:500;font-size:18px;letter-spacing:1px}
.about-photo{left:685px;top:816px;width:353px;height:355px;background:linear-gradient(135deg,#8fb2d6,#3a6fae 55%,#1c3a6e)}
.dots{width:50px;height:38px;background-image:radial-gradient(var(--white) 1.2px,transparent 1.4px);background-size:8px 8px}
.badge{left:612px;top:1080px;width:139px;height:56px;background:var(--blue);border-radius:4px;display:flex;align-items:center;gap:8px;padding-left:14px}
.badge b{font-family:"Roboto",sans-serif;font-size:30px}
.badge span{font-size:12px;line-height:14px}
.services-title{left:157px;top:1408px;font-size:40px}
.services-rule{left:150px;top:1460px;width:107px;height:3px;background:var(--white)}
.services-intro{left:465px;top:1404px;width:480px;font-size:18px;line-height:27px;font-weight:500}
.service{width:262px}
.service svg{display:block;margin-bottom:14px}
.service h3{font-size:18px;font-weight:700;margin-bottom:12px}
.service p{font-size:15px;line-height:22.5px;color:#d5e2f5}
.service .cap{margin-top:14px;font-size:15px;font-weight:500}
.expert-photo{left:214px;top:2235px;width:353px;height:354px;background:linear-gradient(160deg,#2b4b78,#122a52 60%,#a7712e)}
.expert-title{left:656px;top:2240px;width:400px;font-weight:800;font-size:37px;line-height:41px;color:var(--ink)}
.expert-text{left:656px;top:2380px;width:388px;font-size:15.5px;line-height:23px;color:var(--muted)}
.expert-text p+p{margin-top:12px}
.btn-expert{left:656px;top:2538px;width:190px;height:51px;background:var(--blue);font-size:18px;letter-spacing:1px}
.contact-kicker{left:160px;top:2870px;font-size:23px;font-weight:500}
.contact-title{left:160px;top:2902px;font-size:39px;font-weight:800}
.contact-text{left:160px;top:2962px;width:380px;font-size:18px;line-height:28px}
.contact-icon{width:50px;height:50px;border-radius:50%;background:var(--white);display:flex;align-items:center;justify-content:center}
.contact-label{font-size:18px;font-weight:500}
.contact-value{font-size:22px}
.field{left:636px;width:367px;height:41px;border:2px solid #c9ccd6;border-radius:4px;display:flex;align-items:center;gap:14px;padding-left:14px;font-size:14px;font-weight:500}
.field.msg{height:89px;align-items:flex-start;padding-top:11px}
.btn-submit{left:636px;top:3154px;width:137px;height:45px;background:var(--teal);font-size:16px}
.footer-logo{left:160px;top:3468px;font-size:44px}
.footer-logo .logo-mark{width:46px;height:46px}
.footer-text{left:155px;top:3548px;width:270px;font-size:15px;line-height:22px;color:var(--soft)}
.footer-rule{width:2px;height:160px;top:3467px;background:#2a3c72}
.footer-rule::before{content:"";position:absolute;left:0;top:0;width:2px;height:26px;background:var(--white)}
.footer-head{top:3476px;font-family:"Lato",sans-serif;font-weight:900;font-size:15px;letter-spacing:.6px}
.footer-links{top:3505px;list-style:none;font-family:"Lato",sans-serif;font-weight:700;font-size:15px;color:var(--soft)}
.footer-links li{height:31px}
.social{top:3513px;width:31px;height:31px;border-radius:50%;background:var(--white)}
.footer-line{left:105px;top:3679px;width:981px;height:1px;background:#33467a}
.copyright{left:0;width:1200px;top:3705px;text-align:center;font-family:"Lato",sans-serif;font-size:13px;color:var(--soft)}
</style>
</head>
<body>

<div class="abs hero-photo" role="img" aria-label="Aerial photo of a busy city road and market"></div>

<svg class="backdrop" width="1200" height="3757" viewBox="0 0 1200 3757" aria-hidden="true">
  <defs>
    <linearGradient id="servicesFill" x1="0" y1="0" x2="1" y2="1">
      <stop offset="0" stop-color="#062a5a"/>
      <stop offset="1" stop-color="#0a68c8"/>
    </linearGradient>
    <linearGradient id="contactFill" x1="0" y1="0" x2="0" y2="1">
      <stop offset="0" stop-color="#26262e"/>
      <stop offset=".7" stop-color="#1e2230"/>
      <stop offset="1" stop-color="#0d1c48"/>
    </linearGradient>
  </defs>
  <polygon points="0,700 598,649 1200,744 1200,1400 0,1400" fill="#020d1e"/>
  <polyline points="0,700 598,649 1200,744" fill="none" stroke="#1170d6" stroke-width="5"/>
  <polygon points="0,1363 379,1273 1200,1363 1200,2056 802,2152 0,2056" fill="url(#servicesFill)"/>
  <polyline points="0,1363 379,1273 1200,1363" fill="none" stroke="#1170d6" stroke-width="5"/>
  <polyline points="0,2056 802,2152 1200,2056" fill="none" stroke="#1170d6" stroke-width="4"/>
  <polygon points="0,3310 379,3404 1200,3310 1200,3757 0,3757" fill="#0a1a48"/>
  <polygon points="0,2785 802,2690 1200,2785 1200,3310 379,3404 0,3310" fill="url(#contactFill)"/>
  <polyline points="0,2785 802,2690 1200,2785" fill="none" stroke="#1170d6" stroke-width="5"/>
  <polyline points="0,3310 379,3404 1200,3310" fill="none" stroke="#1170d6" stroke-width="5"/>
</svg>
<div class="abs" style="left:0;top:2700px;width:1200px;height:700px" role="img" aria-label="Photo of a business handshake over a city at night"></div>

<header>
  <div class="abs logo site-logo"><span class="logo-mark"></span>ZELMOR</div>
  <nav>
    <span class="abs nav active" style="left:497px">HOME</span>
    <span class="abs nav" style="left:586px">ABOUT US</span>
    <span class="abs nav" style="left:709px">SERVICES</span>
    <span class="abs nav" style="left:825px">TEAM</span>
  </nav>
  <a class="abs btn btn-contact">CONTACT</a>
</header>

<section class="hero">
  <div class="abs play">
    <svg width="72" height="72" viewBox="0 0 72 72"><polygon points="30,25 47,36 30,47" fill="#fff"/></svg>
  </div>
  <div class="abs hero-kicker">WELCOM TO</div>
  <h1 class="abs hero-title">ZELMOR CONSULTING FIRM</h1>
  <a class="abs btn btn-hero">LEARN MORE</a>
</section>

<section class="about">
  <h2 class="abs section-title about-title">ABOUT ZELMOR</h2>
  <div class="abs body-text about-text">
    <p>Lorem Ipsum is simply dummy text of the printing and typesetting industry.</p>
    <p>Lorem Ipsum has been the industry's standard dummy text ever since the 1500s, when an unknown printer took a galley of type and scrambled it to make a type specimen book. unchanged.</p>
  </div>
  <a class="abs btn btn-outline">LEARN MORE</a>
  <div class="abs dots" style="left:667px;top:801px"></div>
  <div class="abs about-photo" role="img" aria-label="Photo of a smiling consultant shaking hands"></div>
  <div class="abs dots" style="left:1004px;top:1146px"></div>
  <div class="abs badge"><b>12</b><span>Years<br>Experience</span></div>
</section>

<section class="services">
  <h2 class="abs section-title services-title">OUR SERVICES</h2>
  <div class="abs services-rule"></div>
  <p class="abs services-intro">Lorem Ipsum is simply dummy text of the printing and typesetting industry. Lorem Ipsum is simply</p>

  <article class="abs service" style="left:159px;top:1518px">
    <svg width="60" height="58" viewBox="0 0 60 58" fill="none" stroke="#fff" stroke-width="2"><path d="M6 54h48"/><rect x="10" y="38" width="8" height="16"/><rect x="26" y="28" width="8" height="26"/><rect x="42" y="18" width="8" height="36"/><path d="M8 28L24 14l10 8L50 6M42 6h8v8"/></svg>
    <h3>Growth Strategy &nbsp;›</h3>
    <p>Lorem Ipsum is simply dummy text the printing and typesetting. Lorem Ipsum is simply.</p>
    <div class="cap">Capabilities &nbsp;⌄</div>
  </article>
  <article class="abs service" style="left:469px;top:1518px">
    <svg width="60" height="58" viewBox="0 0 60 58" fill="none" stroke="#fff" stroke-width="2"><path d="M6 54h48"/><rect x="10" y="38" width="8" height="16"/><rect x="26" y="28" width="8" height="26"/><rect x="42" y="18" width="8" height="36"/><path d="M8 28L24 14l10 8L50 6M42 6h8v8"/></svg>
    <h3>Growth Strategy &nbsp;›</h3>
    <p>Lorem Ipsum is simply dummy text the printing and typesetting. Lorem Ipsum is simply.</p>
    <div class="cap">Capabilities &nbsp;⌄</div>
  </article>
  <article class="abs service" style="left:786px;top:1518px">
    <svg width="60" height="58" viewBox="0 0 60 58" fill="none" stroke="#fff" stroke-width="2"><path d="M6 54h48"/><rect x="10" y="38" width="8" height="16"/><rect x="26" y="28" width="8" height="26"/><rect x="42" y="18" width="8" height="36"/><path d="M8 28L24 14l10 8L50 6M42 6h8v8"/></svg>
    <h3>Growth Strategy &nbsp;›</h3>
    <p>Lorem Ipsum is simply dummy text the printing and typesetting. Lorem Ipsum is simply.</p>
    <div class="cap">Capabilities &nbsp;⌄</div>
  </article>
  <article class="abs service" style="left:159px;top:1782px">
    <svg width="60" height="58" viewBox="0 0 60 58" fill="none" stroke="#fff" stroke-width="2"><path d="M6 54h48"/><rect x="10" y="38" width="8" height="16"/><rect x="26" y="28" width="8" height="26"/><rect x="42" y="18" width="8" height="36"/><path d="M8 28L24 14l10 8L50 6M42 6h8v8"/></svg>
    <h3>Growth Strategy &nbsp;›</h3>
    <p>Lorem Ipsum is simply dummy text the printing and typesetting. Lorem Ipsum is simply.</p>
    <div class="cap">Capabilities &nbsp;⌄</div>
  </article>
  <article class="abs service" style="left:469px;top:1782px">
    <svg width="60" height="58" viewBox="0 0 60 58" fill="none" stroke="#fff" stroke-width="2"><path d="M6 54h48"/><rect x="10" y="38" width="8" height="16"/><rect x="26" y="28" width="8" height="26"/><rect x="42" y="18" width="8" height="36"/><path d="M8 28L24 14l10 8L50 6M42 6h8v8"/></svg>
    <h3>Growth Strategy &nbsp;›</h3>
    <p>Lorem Ipsum is simply dummy text the printing and typesetting. Lorem Ipsum is simply.</p>
    <div class="cap">Capabilities &nbsp;⌄</div>
  </article>
  <article class="abs service" style="left:786px;top:1782px">
    <svg width="60" height="58" viewBox="0 0 60 58" fill="none" stroke="#fff" stroke-width="2"><path d="M6 54h48"/><rect x="10" y="38" width="8" height="16"/><rect x="26" y="28" width="8" height="26"/><rect x="42" y="18" width="8" height="36"/><path d="M8 28L24 14l10 8L50 6M42 6h8v8"/></svg>
    <h3>Growth Strategy &nbsp;›</h3>
    <p>Lorem Ipsum is simply dummy text the printing and typesetting. Lorem Ipsum is simply.</p>
    <div class="cap">Capabilities &nbsp;⌄</div>
  </article>
</section>

<section class="process">
  <div class="abs expert-photo" role="img" aria-label="Photo of a business hand with a glowing growth chart"></div>
  <h2 class="abs expert-title">Expert marketing consulting grow your business</h2>
  <div class="abs expert-text">
    <p>Lorem Ipsum is simply dummy text of the printing and typesetting industry.</p>
    <p>Lorem Ipsum has been the industry's standard dummy text ever since the 1500s, when an unknown printer took a galley of type and scrambled.</p>
  </div>
  <a class="abs btn btn-expert">LEARN MORE</a>
</section>

<section class="contact">
  <div class="abs contact-kicker">Get in touch</div>
  <h2 class="abs contact-title">Contact Us</h2>
  <p class="abs contact-text">Lorem Ipsum is simply dummy text of the printing and typesetting industry.</p>

  <div class="abs contact-icon" style="left:160px;top:3051px">
    <svg width="26" height="26" viewBox="0 0 24 24"><path d="M6.6 10.8a15 15 0 0 0 6.6 6.6l2.2-2.2a1 1 0 0 1 1-.25 11.4 11.4 0 0 0 3.6.57 1 1 0 0 1 1 1V20a1 1 0 0 1-1 1A17 17 0 0 1 3 4a1 1 0 0 1 1-1h3.5a1 1 0 0 1 1 1c0 1.25.2 2.45.57 3.57a1 1 0 0 1-.25 1z" fill="#0b3fa8"/></svg>
  </div>
  <div class="abs contact-label" style="left:234px;top:3052px">Phone Number</div>
  <div class="abs contact-value" style="left:234px;top:3077px;font-weight:700">+10 555 01 234</div>

  <div class="abs contact-icon" style="left:160px;top:3142px">
    <svg width="26" height="26" viewBox="0 0 24 24"><path d="M6.6 10.8a15 15 0 0 0 6.6 6.6l2.2-2.2a1 1 0 0 1 1-.25 11.4 11.4 0 0 0 3.6.57 1 1 0 0 1 1 1V20a1 1 0 0 1-1 1A17 17 0 0 1 3 4a1 1 0 0 1 1-1h3.5a1 1 0 0 1 1 1c0 1.25.2 2.45.57 3.57a1 1 0 0 1-.25 1z" fill="#0b3fa8"/></svg>
  </div>
  <div class="abs contact-label" style="left:234px;top:3143px">Write Email Us</div>
  <div class="abs contact-value" style="left:234px;top:3170px">mail@companyname.example</div>

  <form>
    <div class="abs field" style="top:2881px">
      <svg width="16" height="16" viewBox="0 0 16 16" fill="none" stroke="#fff" stroke-width="1.3"><circle cx="8" cy="5" r="3"/><path d="M2 15c0-3.5 2.7-5.5 6-5.5s6 2 6 5.5"/></svg>Name</div>
    <div class="abs field" style="top:2938px">
      <svg width="16" height="16" viewBox="0 0 16 16" fill="none" stroke="#fff" stroke-width="1.3"><rect x="1.5" y="3" width="13" height="10"/><path d="M1.5 3l6.5 6 6.5-6"/></svg>Email</div>
    <div class="abs field" style="top:2993px">
      <svg width="16" height="16" viewBox="0 0 24 24" fill="none" stroke="#fff" stroke-width="1.8"><path d="M6.6 10.8a15 15 0 0 0 6.6 6.6l2.2-2.2 5 1.3V20A17 17 0 0 1 3 4h4.5l1.3 5z"/></svg>Phone</div>
    <div class="abs field msg" style="top:3050px">
      <svg width="16" height="16" viewBox="0 0 16 16" fill="none" stroke="#fff" stroke-width="1.3"><rect x="1.5" y="6" width="13" height="8"/><path d="M4 6V2h8v4M4 9h8"/></svg>Message</div>
    <a class="abs btn btn-submit">SUBMIT</a>
  </form>
</section>

<footer>
  <div class="abs logo footer-logo"><span class="logo-mark"></span>ZELMOR</div>
  <p class="abs footer-text">Lorem Ipsum is simply dummy text of the printing and typesetting industry. Lorem Ipsum is simply.</p>

  <div class="abs footer-rule" style="left:458px"></div>
  <div class="abs footer-head" style="left:487px">NAVIGATION</div>
  <ul class="abs footer-links" style="left:487px">
    <li>Home</li><li>About Us</li><li>Services</li><li>Team</li>
  </ul>

  <div class="abs footer-rule" style="left:697px"></div>
  <div class="abs footer-head" style="left:726px">RESOURCES</div>
  <ul class="abs footer-links" style="left:726px">
    <li>Services</li><li>Services</li><li>Blog</li><li>Contact</li>
  </ul>

  <div class="abs footer-rule" style="left:926px"></div>
  <div class="abs footer-head" style="left:955px">FOLLOW US</div>
  <a class="abs social" style="left:956px" aria-label="Social profile one"></a>
  <a class="abs social" style="left:992px" aria-label="Social profile two"></a>

  <div class="abs footer-line"></div>
  <div class="abs copyright">Copyright © 2023 Company. All rights reserved.</div>
</footer>

</body>
</html>
```